Kerno Solutions: searching for a flyer to trow in letterboxes for properties we are interested in

Hello ,

Introduction:
We are a company based in Luxembourg called "Kerno Solutions". We are specialized in buying properties on which we develop and build constructions before selling them.

Informations for the flyer:
We need a flyer to trow into the letter boxes of property owners letting them know that we are interested in buying their property, if they are interested they can give us a call.

The text for the flyer/letter is in the attachment called >>2020-03-11_KS_Text for flyer,letter there might be slight changes<<.

We need to look competent, professional and financially stable.

The flyer needs to be short and not over welling with information otherwise it will land in the trash.

We have decided that we don't want real pictures on the flyer, but shapes of any kind, blue prints, drawings are fine.

Format should be in DIN A4. We plan to print the flyer on both sides in two different languages, in other words the design will be the same on both sides only the text will be in a different language.

I also added our current logo and here is the design of the website that is under construction at the moment http://www.kernosolutions-example.lu/. The logo's color can be changed into a different blue or uni color (all white or all black).
Updates

Hi, First time user the howl thing started faster as expected. Furthermore, I need to catch my boss to discust the project with him and he is on a lot of meetings. Please give us a little bit more time. Thanks

Target Market(s)

Property owners

Requirements
Must have
• email, phone number, tax number (RCS), Tax number , matriculation and address.
see word file in attachment for information
Nice to have
• Our company logo, in one form or an other, you can be creative, the logo is in the attachment.
Should not have
• Real pictures

```html
<!DOCTYPE html>
<html lang="en">
<head>
<meta charset="utf-8">
<title>Kerno Solutions – Flyer</title>
<link rel="stylesheet" href="https://fonts.googleapis.com/css2?family=Bebas+Neue&display=swap">
<style>
  :root {
    --backdrop: #1f1f21;
    --paper: #ffffff;
    --brand-blue: #0f4f74;
    --brand-blue-light: #1a6a9c;
    --ink: #2b2b2b;
    --ink-strong: #111111;
    --sky-top: #5f8fd0;
    --sky-low: #b9d2ea;
    --lawn: #4f9a3a;
  }
  * { margin: 0; padding: 0; box-sizing: border-box; }
  html, body {
    width: 900px; height: 1200px; overflow: hidden;
    background: var(--backdrop);
    font-family: "Bebas Neue", "Oswald", sans-serif;
  }
  .flyer {
    position: absolute; left: 88px; top: 87px;
    width: 725px; height: 1026px;
    background: var(--paper);
    overflow: hidden;
  }
  .flyer-shapes { position: absolute; inset: 0; width: 725px; height: 1026px; }
  .brand {
    position: absolute; left: 40px; top: 186px;
    display: flex; align-items: center; gap: 12px;
  }
  .brand-square { width: 30px; height: 30px; background: var(--brand-blue-light); }
  .brand-name {
    font-size: 46px; line-height: 1; color: var(--brand-blue-light);
    letter-spacing: 0.5px;
  }
  .pitch { position: absolute; left: 28px; line-height: 1; white-space: nowrap; }
  .pitch-lead { top: 667px; font-size: 33px; color: var(--ink); }
  .pitch-band { top: 707px; font-size: 46px; color: var(--paper); }
  .pitch-line-1 { top: 764px; font-size: 33px; color: var(--ink); }
  .pitch-line-2 { top: 801px; font-size: 33px; color: var(--ink); }
  .pitch-call { top: 841px; font-size: 64px; color: var(--paper); }
  .registry {
    position: absolute; right: 36px; top: 846px;
    text-align: right; font-size: 20px; line-height: 29px;
    color: var(--brand-blue);
  }
  .contact-bar {
    position: absolute; left: 0; bottom: 0; width: 725px; height: 90px;
    background: var(--brand-blue); color: var(--paper);
  }
  .contact-row {
    position: absolute; left: 0; right: 0;
    display: flex; justify-content: center; align-items: center; gap: 12px;
    line-height: 1; white-space: nowrap;
  }
  .contact-row--main { top: 10px; font-size: 29px; }
  .contact-row--address { top: 53px; font-size: 21px; gap: 8px; }
  .contact-icon { width: 30px; height: 30px; flex: none; }
  .contact-row--address .contact-icon { width: 24px; height: 24px; }
  .contact-gap { width: 8px; }
</style>
</head>
<body>
<main class="flyer">
  <svg class="flyer-shapes" viewBox="0 0 1336 1890" aria-hidden="false">
    <defs>
      <linearGradient id="scene-main" x1="0" y1="0" x2="0" y2="1">
        <stop offset="0" stop-color="var(--sky-top)"/>
        <stop offset="0.45" stop-color="var(--sky-low)"/>
        <stop offset="0.62" stop-color="#d8dde2"/>
        <stop offset="0.78" stop-color="#9ea6ad"/>
        <stop offset="1" stop-color="var(--lawn)"/>
      </linearGradient>
      <linearGradient id="scene-homes" x1="0" y1="0" x2="0" y2="1">
        <stop offset="0" stop-color="#3f73c4"/>
        <stop offset="0.6" stop-color="#a39a90"/>
        <stop offset="1" stop-color="#6c8a3e"/>
      </linearGradient>
      <linearGradient id="scene-office" x1="0" y1="0" x2="0" y2="1">
        <stop offset="0" stop-color="#cfe0ee"/>
        <stop offset="0.5" stop-color="#3a4658"/>
        <stop offset="1" stop-color="#d9a928"/>
      </linearGradient>
    </defs>

    <polygon class="scene-main" role="img" aria-label="Photo of a modern two-storey house with front gate, trees and lawn"
      fill="url(#scene-main)" points="1025,0 1336,0 1336,730 667,1400 290,1020 560,560"/>
    <polygon class="accent-diamond" role="img" aria-label="Blue architectural floor plan drawing"
      fill="#0f5f8c" fill-opacity="0.88" points="259,532 497,770 277,1020 25,767"/>
    <polygon class="accent-triangle" fill="var(--brand-blue)" points="1336,760 1336,1070 1179,918"/>
    <polygon class="scene-homes" role="img" aria-label="Photo of suburban family houses with garages"
      fill="url(#scene-homes)" points="1172,922 1336,1070 1336,1240 1137,1400 937,1160"/>
    <polygon class="scene-office" role="img" aria-label="Photo of a modern office building at dusk"
      fill="url(#scene-office)" points="917,1180 1157,1420 917,1660 675,1418"/>

    <polygon class="pitch-band-shape" fill="var(--brand-blue)" points="0,1290 497,1290 592,1388 0,1388"/>
    <polygon class="call-band-shape" fill="var(--brand-blue)" points="0,1538 737,1538 857,1658 0,1658"/>
  </svg>

  <div class="brand">
    <span class="brand-square"></span>
    <span class="brand-name">Kerno Solutions</span>
  </div>

  <p class="pitch pitch-lead">If you are</p>
  <p class="pitch pitch-band">Interested in</p>
  <p class="pitch pitch-line-1">Selling your property</p>
  <p class="pitch pitch-line-2">then the day come so</p>
  <p class="pitch pitch-call">Give us a call</p>

  <p class="registry">RCS:<br>Willbeadded</p>

  <footer class="contact-bar">
    <div class="contact-row contact-row--main">
      <svg class="contact-icon" viewBox="0 0 30 30" aria-hidden="true">
        <circle cx="15" cy="15" r="15" fill="#fff"/>
        <path d="M10 7.5c1-.6 1.8-.3 2.3.6l1.3 2.4c.4.8.2 1.5-.5 2l-1 .7c.7 1.9 2 3.4 3.8 4.4l.8-.9c.6-.7 1.3-.8 2.1-.3l2.3 1.5c.8.6 1 1.4.3 2.3l-1 1.1c-1 1-2.6 1.2-4.1.4-3.8-2-6.5-5.1-7.9-9.1-.5-1.5-.1-3.1 1-4z" fill="var(--brand-blue)"/>
      </svg>
      <span>691 000 555</span>
      <span class="contact-gap"></span>
      <svg class="contact-icon" viewBox="0 0 30 30" aria-hidden="true">
        <circle cx="15" cy="15" r="15" fill="#fff"/>
        <rect x="8" y="10" width="14" height="10" rx="1.5" fill="var(--brand-blue)"/>
        <path d="M8.5 11l6.5 5 6.5-5" fill="none" stroke="#fff" stroke-width="1.4"/>
      </svg>
      <span>info@kernosolutions-example.lu</span>
    </div>
    <div class="contact-row contact-row--address">
      <svg class="contact-icon" viewBox="0 0 24 24" aria-hidden="true">
        <circle cx="12" cy="12" r="12" fill="#fff"/>
        <path d="M12 5a4.6 4.6 0 0 0-4.6 4.6c0 3.4 4.6 8.6 4.6 8.6s4.6-5.2 4.6-8.6A4.6 4.6 0 0 0 12 5z" fill="var(--brand-blue)"/>
        <circle cx="12" cy="9.6" r="1.7" fill="#fff"/>
      </svg>
      <span>18 Rue des Artisans, L-3900 Exampleville</span>
    </div>
  </footer>
</main>
</body>
</html>
```